Quiet Harbor Podcast Business Card Design

Needing a business card with the logo design provided for Quiet Harbor Podcast. I am looking for a modern style that fits the current logo.

Info:
Name: Teodor Vask
Title: Creator/Host
Email: teodor@quietharborcast.com
Phone: (555) 274-9163
www.quietharborcast.com
Twitter: @qharborcast
Instagram: @quietharborcastshow
Facebook: Quiet Harbor Podcast

Industry/Entity Type

Business

Font styles to use
Sans Serif

Colors
000000
ffffff

Requirements
Must have
• modern, clean design
Nice to have
• social media contact info

```html
<!DOCTYPE html>
<html lang="en">
<head>
<meta charset="utf-8">
<title>Quiet Harbor Podcast – Business Card</title>
<link href="https://fonts.googleapis.com/css2?family=Lato:wght@300;400;700&display=swap" rel="stylesheet">
<style>
  :root {
    --ink: #1e1e1e;
    --text: #3a3a3a;
    --paper: #ffffff;
    --backdrop: #e6e4e1;
    --rule: #8a8a8a;
  }
  * { box-sizing: border-box; margin: 0; padding: 0; }
  html, body {
    width: 1200px; height: 1000px; overflow: hidden;
    background: var(--backdrop);
    font-family: "Lato", sans-serif;
  }
  .canvas { position: relative; width: 1200px; height: 1000px; }
  .card {
    position: absolute; left: 240px; width: 696px; height: 397px;
    background: var(--paper); border-radius: 22px;
  }
  .card--front { top: 83px; }
  .card--back { top: 520px; }

  .brand {
    position: absolute; text-align: center; color: var(--ink);
    font-family: "Lato", sans-serif; font-weight: 700;
  }
  .card--front .brand { left: 20px; width: 316px; top: 218px; }
  .brand__mark {
    display: block; margin: 0 auto 14px; width: 58px; height: 58px;
    background: var(--ink);
  }
  .card--front .brand__name { font-size: 27px; letter-spacing: 0.2px; line-height: 1; }
  .card--front .brand__tag { font-size: 11px; letter-spacing: 4.5px; margin-top: 6px; }

  .divider {
    position: absolute; left: 334px; top: 100px; width: 1px; height: 197px;
    background: linear-gradient(to bottom, transparent, var(--rule) 20%, var(--rule) 80%, transparent);
  }
  .person { position: absolute; left: 363px; top: 101px; color: var(--ink); }
  .person__name { font-size: 21px; font-weight: 400; letter-spacing: 0.6px; line-height: 1.1; }
  .person__title { font-size: 16px; font-weight: 400; margin-top: 3px; }

  .contact-list { position: absolute; left: 363px; list-style: none; color: var(--text); }
  .contact-list--direct { top: 160px; }
  .contact-list--social { top: 235px; }
  .contact-list li {
    display: flex; align-items: center; height: 21px;
    font-size: 15.5px; font-weight: 300;
  }
  .contact-list .icon { width: 13px; height: 13px; margin-right: 18px; flex: none; fill: var(--ink); }

  .card--back .brand { left: 0; width: 100%; top: 96px; }
  .card--back .brand__mark { width: 110px; height: 110px; margin-bottom: 38px; }
  .card--back .brand__name { font-size: 43px; letter-spacing: 0.3px; line-height: 1; }
  .card--back .brand__tag { font-size: 17px; letter-spacing: 9px; margin-top: 10px; padding-left: 9px; }
</style>
</head>
<body>
<main class="canvas">
  <section class="card card--front">
    <div class="brand">
      <span class="brand__mark"></span>
      <div class="brand__name">QUIET HARBOR</div>
      <div class="brand__tag">PODCAST</div>
    </div>
    <div class="divider"></div>
    <div class="person">
      <div class="person__name">TEODOR VASK</div>
      <div class="person__title">Creator/Host</div>
    </div>
    <ul class="contact-list contact-list--direct">
      <li><svg class="icon" viewBox="0 0 16 16"><path d="M3.6 1.2l2.2 2.6-1.2 1.8c.9 2 2.3 3.4 4.2 4.3l1.7-1.2 2.7 2.2-1.3 2.2C6.5 13.2 2.8 9.4 1.3 3z"/></svg>(555) 274-9163</li>
      <li><svg class="icon" viewBox="0 0 16 16"><path d="M1 3h14v1.2L8 9 1 4.2z"/><path d="M1 5.8l7 4.8 7-4.8V13H1z"/></svg>teodor@quietharborcast.com</li>
      <li><svg class="icon" viewBox="0 0 16 16"><circle cx="8" cy="8" r="6.5" fill="none" stroke="#1e1e1e" stroke-width="1.6"/><ellipse cx="8" cy="8" rx="2.6" ry="6.5" fill="none" stroke="#1e1e1e" stroke-width="1.2"/><path d="M1.5 8h13" stroke="#1e1e1e" stroke-width="1.2"/></svg>www.quietharborcast.com</li>
    </ul>
    <ul class="contact-list contact-list--social">
      <li><svg class="icon" viewBox="0 0 16 16"><rect x="1" y="1" width="14" height="14" rx="2"/></svg>Quiet Harbor Podcast</li>
      <li><svg class="icon" viewBox="0 0 16 16"><rect x="1" y="1" width="14" height="14" rx="2"/></svg>@qharborcast</li>
      <li><svg class="icon" viewBox="0 0 16 16"><rect x="1" y="1" width="14" height="14" rx="2"/></svg>@quietharborcastshow</li>
    </ul>
  </section>

  <section class="card card--back">
    <div class="brand">
      <span class="brand__mark"></span>
      <div class="brand__name">QUIET HARBOR</div>
      <div class="brand__tag">PODCAST</div>
    </div>
  </section>
</main>
</body>
</html>
```